HPS business cards

(Generators . Lighting Towers . De-watering Pumps . Compressors) put under the logo please. my details are Owen Pritchard (Director) 0461527390 harbourpinesupply@postvale.net

```html
<!DOCTYPE html>
<html lang="en">
<head>
<meta charset="utf-8">
<title>HPS business cards</title>
<link href="https://fonts.googleapis.com/css2?family=Montserrat:wght@400;500;600;700&display=swap" rel="stylesheet">
<style>
  :root {
    --backdrop: #2b2b2d;
    --card: #151515;
    --gold: #e49a2a;
    --silver: #d4d4d4;
    --text: #ededed;
  }
  * { box-sizing: border-box; margin: 0; padding: 0; }
  html, body {
    width: 1200px; height: 875px; overflow: hidden;
    background: var(--backdrop);
    font-family: "Montserrat", sans-serif;
  }
  .sheet {
    width: 1200px; height: 875px;
    display: flex; align-items: center; justify-content: center; gap: 40px;
  }
  .card {
    width: 540px; height: 310px;
    background: var(--card);
    border-radius: 24px;
    box-shadow: 0 20px 40px rgba(0,0,0,.45);
    position: relative;
  }
  /* front */
  .card--front {
    display: flex; flex-direction: column; align-items: center; justify-content: center;
  }
  .brand {
    display: flex; align-items: center; gap: 12px;
    color: var(--gold); font-weight: 700; letter-spacing: 1px;
  }
  .brand__mark { width: 14px; height: 14px; background: var(--gold); }
  .card--front .brand { font-size: 30px; }
  .brand-rule { width: 360px; height: 1px; background: var(--silver); opacity: .6; margin: 16px 0 34px; }
  .services { color: var(--gold); font-weight: 600; font-size: 13px; letter-spacing: .3px; }
  /* back */
  .card--back { display: flex; align-items: center; padding: 0 34px; }
  .card--back .brand { font-size: 17px; gap: 8px; }
  .card--back .brand__mark { width: 10px; height: 10px; }
  .back-logo { display: flex; flex-direction: column; align-items: flex-start; }
  .back-logo .brand-rule { width: 190px; margin: 10px 0 0; }
  .divider { width: 1px; height: 120px; background: var(--gold); margin: 0 22px; }
  .contact__name { color: var(--gold); font-weight: 700; font-size: 20px; }
  .contact__role { color: var(--text); font-size: 12px; margin: 2px 0 12px; }
  .contact__list { list-style: none; }
  .contact__item {
    display: flex; align-items: center; gap: 8px;
    color: var(--text); font-size: 11.5px; line-height: 20px;
  }
  .contact__item svg { width: 11px; height: 11px; fill: var(--gold); flex: none; }
</style>
</head>
<body>
<main class="sheet">
  <section class="card card--front">
    <div class="brand"><span class="brand__mark"></span>HARBOUR PINE SUPPLY</div>
    <div class="brand-rule"></div>
    <p class="services">Generators . Lighting Towers . De-watering Pumps . Compressors</p>
  </section>

  <section class="card card--back">
    <div class="back-logo">
      <div class="brand"><span class="brand__mark"></span>HARBOUR PINE SUPPLY</div>
      <div class="brand-rule"></div>
    </div>
    <div class="divider"></div>
    <div class="contact">
      <h1 class="contact__name">Owen Pritchard</h1>
      <p class="contact__role">Director</p>
      <ul class="contact__list">
        <li class="contact__item">
          <svg viewBox="0 0 24 24"><path d="M6.6 10.8a15 15 0 0 0 6.6 6.6l2.2-2.2a1 1 0 0 1 1-.25 11.4 11.4 0 0 0 3.6.57 1 1 0 0 1 1 1V20a1 1 0 0 1-1 1A17 17 0 0 1 3 4a1 1 0 0 1 1-1h3.5a1 1 0 0 1 1 1c0 1.25.2 2.45.57 3.57a1 1 0 0 1-.25 1z"/></svg>
          0461527390
        </li>
        <li class="contact__item">
          <svg viewBox="0 0 24 24"><path d="M2 5h20v14H2z M2 5l10 8 10-8" /></svg>
          harbourpinesupply@postvale.net
        </li>
        <li class="contact__item">
          <svg viewBox="0 0 24 24"><circle cx="12" cy="12" r="10"/></svg>
          harbourpinesupply.com
        </li>
      </ul>
    </div>
  </section>
</main>
</body>
</html>
```